Recycling Exhibition Web Design Project

We are developing a new website for a exhibition we have just taken over. The previous site is very basic and we require a complete redesign. The site should be designed to engage with and attract those who work in or provide services to the multibillion dollar wastes and recycling industry in the Asia pacific region. These will include Federal & State Governments, City councils, private sector, industry associations and other key bodies, education facilities.

KTLO is the premier waste and recycling event in the Asia Pacific region and known as place where the industry meets to share innovations, gain knowledge, to network and do business.
• Innovation
• Knowledge transfer
• Industry Networking
• Trade
Key point: need to reflect that 2012 show will attract large numbers of quality visitors from across wide range of the industry – city councils, facilities managers, etc

Site should deliver 3 key objectives.
1. Stimulate interest those who work in or provide services to the wastes and recycling industry by providing simple to access, relevant and topical information about the Expo, the Seminars, the Key Features, the sub activities and the key benefits to them.
2. Provide a platform that supports / improves EP by providing a range of interactive components – ie floor plan / video. In addition options for sales enquiries, registration, general feedback
3. Provide a way to highlight / showcase sponsors, show features and other key assets. (possibly a carousel above the fold)

We really like the dunmar website so a take on this could be good (http://www.dunmar-example.com.au/). Also we want to try to reinforce the brand so we should use the event as the hero image/banner.

Previous website - http://www.ktlo-example.com.au/

Target Market(s)

The site should be designed to engage with and attract those who work in or provide services to the multibillion dollar wastes and recycling industry

Industry/Entity Type

Recycling

Requirements
Must have
• The icons on the current site work quite well so inclusion as CTAs would be preferable.

Other key areas are

• Seminar Delegate & Visitor Registration
• Exhibitor Prospectus
• Floorplan
• Conference / Seminar content
• Social media + blog

Site visitors will need to feel like they are part of a community.
Site should reflect/display key industry stats & stats from 2011 expo

Please see the attached brief for more details and site map for menu items.

```html
<!DOCTYPE html>
<html lang="en">
<head>
<meta charset="utf-8">
<title>KTLO – Waste &amp; Recycling Event</title>
<link rel="stylesheet" href="https://fonts.googleapis.com/css2?family=Cinzel:wght@400;500;600&display=swap">
<style>
  :root {
    --page-bg: #cdcdcd;
    --header-top: #1c9f30;
    --header-bottom: #0f8a26;
    --header-rule: #0b6a1c;
    --ink: #141414;
    --ink-soft: #222222;
    --body-text: #f4f4f4;
    --frame: #1e1e1e;
    --screen-light: #b4b4b4;
    --screen-dark: #9c9c9c;
    --arrow-box: #1a1a1a;
    --arrow: #9a9a9a;
  }
  * { margin: 0; padding: 0; box-sizing: border-box; }
  html, body { width: 1200px; height: 900px; overflow: hidden; }
  body {
    background: var(--page-bg);
    font-family: "Cinzel", "Times New Roman", serif;
    color: var(--ink);
    position: relative;
  }
  .site-header {
    position: absolute; left: 0; top: 0; width: 1200px; height: 129px;
    background: linear-gradient(to bottom, var(--header-top), var(--header-bottom));
    border-bottom: 2px solid var(--header-rule);
    box-shadow: 0 2px 6px rgba(0,0,0,0.3);
  }
  .brand {
    position: absolute; left: 36px; top: 38px;
    display: flex; align-items: center; gap: 16px;
  }
  .brand-mark { width: 30px; height: 30px; background: var(--ink); }
  .brand-name { font-size: 46px; font-weight: 500; color: var(--ink); letter-spacing: 2px; }
  .main-nav {
    position: absolute; left: 517px; top: 46px;
    display: flex; gap: 31px;
  }
  .main-nav a {
    color: var(--ink); text-decoration: none; font-size: 26px;
    text-shadow: 0 2px 4px rgba(0,0,0,0.35);
  }
  .carousel {
    position: absolute; left: 298px; top: 143px; width: 606px; height: 259px;
    background: var(--frame);
    box-shadow: 0 2px 8px rgba(0,0,0,0.45);
  }
  .carousel-screen {
    position: absolute; left: 83px; top: 25px; width: 438px; height: 208px;
    background: linear-gradient(160deg, var(--screen-light) 0%, var(--screen-light) 55%, var(--screen-dark) 56%, var(--screen-dark) 100%);
  }
  .carousel-arrow {
    position: absolute; top: 76px; width: 41px; height: 55px; background: var(--arrow-box);
  }
  .carousel-arrow.prev { left: 83px; }
  .carousel-arrow.next { left: 480px; }
  .carousel-arrow svg, .carousel-play { position: absolute; }
  .carousel-play { left: 283px; top: 71px; }
  .section-title {
    position: absolute; left: 0; width: 1200px; top: 403px;
    text-align: center; font-size: 26px; font-weight: 500;
    text-shadow: 0 2px 4px rgba(0,0,0,0.3);
  }
  .recycle-item {
    position: absolute; top: 446px; width: 120px; text-align: center;
    font-size: 15px; line-height: 18px; font-weight: 500;
    text-shadow: 0 1px 3px rgba(0,0,0,0.3);
  }
  .recycle-item svg { display: block; margin: 0 auto 4px; }
  .feature-column { position: absolute; top: 594px; }
  .feature-column h2 {
    font-size: 33px; font-weight: 500; margin-bottom: 16px;
    text-shadow: 0 2px 4px rgba(0,0,0,0.35);
  }
  .feature-column p {
    color: var(--body-text);
    text-shadow: 0 1px 3px rgba(0,0,0,0.35);
  }
  .feature-column.left { left: 39px; width: 345px; }
  .feature-column.left h2 { padding-left: 34px; }
  .feature-column.left p { font-size: 21px; line-height: 25px; }
  .feature-column.center { left: 449px; width: 300px; text-align: center; }
  .feature-column.center p { font-size: 18px; line-height: 22px; padding: 0 6px; }
  .feature-column.right { left: 800px; width: 340px; text-align: right; }
  .feature-column.right h2 { text-align: center; padding-left: 40px; }
  .feature-column.right p { font-size: 21px; line-height: 25px; }
</style>
</head>
<body>
  <header class="site-header">
    <div class="brand">
      <span class="brand-mark"></span>
      <span class="brand-name">KTLO</span>
    </div>
    <nav class="main-nav">
      <a href="#">Home</a>
      <a href="#">Contact Us</a>
      <a href="#">Floor Plan</a>
      <a href="#">Sponsors</a>
    </nav>
  </header>

  <section class="carousel" aria-label="Featured video carousel">
    <div class="carousel-screen" role="img" aria-label="Featured event video"></div>
    <div class="carousel-arrow prev">
      <svg width="41" height="55" viewBox="0 0 41 55"><polygon points="26,17 26,38 14,27.5" fill="var(--arrow)"/></svg>
    </div>
    <div class="carousel-arrow next">
      <svg width="41" height="55" viewBox="0 0 41 55"><polygon points="15,17 15,38 27,27.5" fill="var(--arrow)"/></svg>
    </div>
    <svg class="carousel-play" width="50" height="72" viewBox="0 0 50 72">
      <polygon points="4,2 4,70 48,36" fill="#8c8c8c"/>
    </svg>
  </section>

  <h1 class="section-title">What we Recycle</h1>

  <div class="recycle-item" style="left:367px;">
    <svg width="56" height="56" viewBox="0 0 56 56"><circle cx="28" cy="28" r="22" fill="none" stroke="var(--ink)" stroke-width="8"/></svg>
    Recycled<br>Products
  </div>
  <div class="recycle-item" style="left:491px;top:446px;">
    <svg width="76" height="66" viewBox="0 0 76 66">
      <polygon points="38,2 74,64 2,64" fill="var(--ink)"/>
      <polygon points="38,16 62,58 14,58" fill="var(--page-bg)"/>
      <circle cx="38" cy="32" r="5" fill="var(--ink)"/>
      <circle cx="30" cy="46" r="5" fill="var(--ink)"/>
      <circle cx="46" cy="46" r="5" fill="var(--ink)"/>
    </svg>
    Hazardous<br>Waste
  </div>
  <div class="recycle-item" style="left:609px;top:448px;">
    <svg width="40" height="62" viewBox="0 0 40 62">
      <path d="M20 3 C9 3 3 11 3 20 C3 29 11 34 12 44 L28 44 C29 34 37 29 37 20 C37 11 31 3 20 3 Z" fill="none" stroke="var(--ink)" stroke-width="2.5"/>
      <path d="M15 44 L17 26 L20 32 L23 26 L25 44" fill="none" stroke="var(--ink)" stroke-width="1.8"/>
      <rect x="12" y="46" width="16" height="4" fill="var(--ink)"/>
      <rect x="12" y="52" width="16" height="4" fill="var(--ink)"/>
      <rect x="15" y="57" width="10" height="4" rx="2" fill="var(--ink)"/>
    </svg>
    Energy<br>from<br>waste
  </div>
  <div class="recycle-item" style="left:702px;">
    <svg width="48" height="68" viewBox="0 0 48 68">
      <rect x="17" y="1" width="14" height="6" fill="var(--ink)"/>
      <rect x="2" y="7" width="44" height="8" rx="2" fill="var(--ink)"/>
      <rect x="4" y="17" width="40" height="48" rx="6" fill="var(--ink)"/>
    </svg>
    Containers
  </div>

  <article class="feature-column left">
    <h2>Lorem Ipsum</h2>
    <p>Shoreditch PBR sartorial sriracha. Aliqua eiusmod portland nisi, bespoke ennui flexitarian laborum. Pickled mcsweeney's fixie butcher typewriter street art sriracha dreamcatcher, gentrify ennui polaroid fugiat helvetica sustainable pork belly.</p>
  </article>
  <article class="feature-column center">
    <h2>Lorem Ipsum</h2>
    <p>Shoreditch PBR sartorial sriracha. Aliqua eiusmod portland nisi, bespoke ennui flexitarian laborum. Pickled mcsweeney's fixie butcher typewriter street art sriracha dreamcatcher, gentrify ennui polaroid fugiat helvetica sustainable pork belly.</p>
  </article>
  <article class="feature-column right">
    <h2>Lorem Ipsum</h2>
    <p>Shoreditch PBR sartorial sriracha. Aliqua eiusmod portland nisi, bespoke ennui flexitarian laborum. Pickled mcsweeney's fixie butcher typewriter street art sriracha dreamcatcher, gentrify ennui polaroid fugiat helvetica sustainable pork belly.</p>
  </article>
</body>
</html>
```